Coconut oil Product for Private Label Creation

We need a product label design for coconut oil.
We will provide you with all the related information(nutrition fact, brand logo, description)
My brand name is Tidewell Pantry and I attached brand logo.
I attached the good example for other products.
In the front, I focus on the freshness of the product on the white background.
We make the real image of coconut in half.
In the back side, we describe the story of the producer and products with his name and signature. In additions, the company name and address, website, Product of Mexico ... etc.

Target Market(s)

20-30 year old lady

Industry/Entity Type

Nutrition

Colors
add136
33a6d7

Requirements
Must have
• 1. Brand Name and logo : Tidewell Pantry
• 2. Certification : QRLB, KOSHER, NON-GMO
• 3. Sentence : 100% fresh organic extra virgin coconut oil - in the front upper
• unrefined, Cold-Pressed, Gluten-Free - in the front bottom
• 4. We prefer to image design the real fresh coconut in half - in the middle front
• Farm to the table icon
• 5. We will describe the story for producer and product - in the back side A
• 6. We will describe the nutrition fact, ingredients, company information, web-site, bar-code in the back side B
Nice to have
• I attached the good example.
• I attached the bottle shape & size. the circumference of bottle : 27 cm,
• the height of the label : 6cm, the diameter of the cap : 6.7cm, capacity : 500ml

```html
<!DOCTYPE html>
<html lang="en">
<head>
<meta charset="utf-8">
<title>Tidewell Pantry – Extra Virgin Coconut Oil Label</title>
<link rel="stylesheet" href="https://fonts.googleapis.com/css2?family=Open+Sans:wght@300;400;600;700&display=swap">
<style>
  :root {
    --page-bg: #f3f4f6;
    --label-bg: #ffffff;
    --brand-green: #add136;
    --brand-green-deep: #7fae2a;
    --brand-blue: #33a6d7;
    --leaf-pale: #e4eec0;
    --coconut-brown: #a9703c;
    --coconut-flesh: #f3eee6;
    --badge-grey: #c9ced6;
    --badge-blue: #3d5f9a;
    --text-grey: #6f7780;
    --social-green: #b9d98a;
    --social-blue: #6b86c2;
    --social-sky: #8fd0ef;
  }
  * { box-sizing: border-box; margin: 0; padding: 0; }
  html, body { width: 1200px; height: 1000px; overflow: hidden; }
  body {
    background: var(--page-bg);
    font-family: "Open Sans", Arial, sans-serif;
    display: flex; align-items: center; justify-content: center;
  }

  .label-wrap {
    display: flex;
    width: 1140px; height: 520px;
    background: var(--label-bg);
    box-shadow: 0 2px 18px rgba(0,0,0,0.06);
  }
  .panel {
    position: relative;
    height: 100%;
    overflow: hidden;
  }
  .panel + .panel { border-left: 1px dashed #e2e5ea; }
  .panel--back-story { width: 360px; }
  .panel--front { width: 420px; }
  .panel--back-info { width: 360px; }

  .palm-frond {
    position: absolute; inset: 0;
    background: radial-gradient(ellipse at 45% 60%, var(--leaf-pale) 0%, rgba(228,238,192,0.5) 45%, rgba(255,255,255,0) 78%);
  }
  .panel-content { position: relative; height: 100%; }

  /* Back A – producer story */
  .story {
    padding: 70px 40px 0;
    color: var(--text-grey);
  }
  .story__title {
    color: var(--brand-green-deep);
    font-size: 22px; font-weight: 700;
    margin-bottom: 14px;
  }
  .story__text { font-size: 14px; line-height: 1.6; margin-bottom: 12px; }
  .social-row {
    position: absolute; left: 40px; bottom: 70px;
    display: flex; gap: 22px;
  }
  .social-dot { width: 34px; height: 34px; border-radius: 50%; }
  .social-dot--green { background: var(--social-green); }
  .social-dot--blue { background: var(--social-blue); }
  .social-dot--sky { background: var(--social-sky); }

  /* Front */
  .cert-column {
    position: absolute; left: 18px; top: 150px;
    display: flex; flex-direction: column; align-items: center; gap: 30px;
  }
  .cert-badge--square { width: 30px; height: 60px; background: var(--badge-blue); border-radius: 3px; }
  .cert-badge--round { width: 36px; height: 36px; border-radius: 50%; border: 3px solid var(--brand-green-deep); }
  .cert-badge--plain { width: 32px; height: 32px; border: 2px solid var(--badge-grey); }

  .front-stack {
    position: absolute; left: 70px; top: 34px; width: 330px;
    display: flex; flex-direction: column; align-items: center;
  }
  .brand-name {
    display: flex; align-items: center; gap: 8px;
    color: var(--brand-green-deep); font-weight: 700; font-size: 24px;
  }
  .brand-dot { width: 18px; height: 18px; border-radius: 50%; background: var(--brand-green); }
  .headline { margin-top: 14px; width: 100%; text-align: center; color: var(--brand-blue); font-weight: 400; }
  .headline__rule-row { display: flex; align-items: center; gap: 10px; }
  .headline__rule { flex: 1; height: 2px; background: var(--brand-blue); }
  .headline__percent { font-size: 21px; }
  .headline__fresh { display: block; font-size: 31px; line-height: 1.15; }
  .headline__virgin { display: block; font-size: 38px; font-weight: 700; line-height: 1.1; }
  .headline__oil { display: block; font-size: 31px; font-weight: 300; letter-spacing: 2px; line-height: 1.2; }
  .headline__bottom-rule { width: 100%; height: 2px; background: var(--brand-blue); margin-top: 4px; }

  .coconut-image {
    margin-top: 10px; width: 230px; height: 140px; border-radius: 6px;
    background: linear-gradient(90deg, var(--coconut-flesh) 0%, #d9b68d 50%, var(--coconut-brown) 100%);
  }
  .feature-pill {
    margin-top: 18px; padding: 3px 12px; border-radius: 12px;
    background: var(--brand-blue); color: #fff; font-size: 12.5px; font-weight: 600;
    white-space: nowrap;
  }

  /* Back B – facts & company */
  .facts { padding: 50px 34px 0; color: #3c4248; }
  .facts-table { border: 2px solid #3c4248; padding: 8px 10px; width: 190px; font-size: 12px; }
  .facts-table__title { font-size: 18px; font-weight: 700; border-bottom: 4px solid #3c4248; padding-bottom: 2px; margin-bottom: 4px; }
  .facts-row { display: flex; justify-content: space-between; border-bottom: 1px solid #9aa1a8; padding: 2px 0; }
  .facts-row:last-child { border-bottom: none; }
  .facts-row--strong { font-weight: 700; }
  .info-text { margin-top: 16px; font-size: 13px; line-height: 1.6; color: var(--text-grey); width: 200px; }
  .info-text strong { color: var(--brand-green-deep); }
</style>
</head>
<body>
  <main class="label-wrap">

    <section class="panel panel--back-story" aria-label="Back side A: producer story">
      <div class="palm-frond" role="img" aria-label="Pale green palm frond in the background"></div>
      <div class="panel-content">
        <div class="story">
          <h2 class="story__title">From Our Grove</h2>
          <p class="story__text">Every jar begins on a small family farm where ripe coconuts are opened by hand and pressed within hours to keep their fresh flavour.</p>
          <p class="story__text">Use it for cooking, baking and gentle skin care.</p>
        </div>
        <div class="social-row" aria-label="Social links">
          <span class="social-dot social-dot--green"></span>
          <span class="social-dot social-dot--blue"></span>
          <span class="social-dot social-dot--sky"></span>
        </div>
      </div>
    </section>

    <section class="panel panel--front" aria-label="Front">
      <div class="palm-frond" role="img" aria-label="Pale green palm frond sweeping across the label background"></div>
      <div class="panel-content">
        <aside class="cert-column" aria-label="Certifications">
          <div class="cert-badge--square" aria-label="Non-GMO certification badge"></div>
          <div class="cert-badge--round" aria-label="QRLB organic certification badge"></div>
          <div class="cert-badge--plain" aria-label="Kosher certification badge"></div>
        </aside>

        <div class="front-stack">
          <div class="brand-name"><span class="brand-dot"></span>Tidewell Pantry</div>

          <h1 class="headline">
            <span class="headline__rule-row">
              <span class="headline__rule"></span>
              <span class="headline__percent">100%</span>
              <span class="headline__rule"></span>
            </span>
            <span class="headline__fresh">FRESH ORGANIC</span>
            <span class="headline__virgin">EXTRA VIRGIN</span>
            <span class="headline__oil">COCONUT OIL</span>
            <span class="headline__bottom-rule" style="display:block"></span>
          </h1>

          <div class="coconut-image" role="img" aria-label="Photo of a fresh coconut split in half beside a whole coconut"></div>

          <p class="feature-pill">Unrefined | Cold-Pressed | Gluten-Free</p>
        </div>
      </div>
    </section>

    <section class="panel panel--back-info" aria-label="Back side B: nutrition and company information">
      <div class="palm-frond" role="img" aria-label="Pale green palm frond in the background"></div>
      <div class="panel-content">
        <div class="facts">
          <div class="facts-table">
            <div class="facts-table__title">Nutrition Facts</div>
            <div class="facts-row"><span>Serving Size 1 Tbsp (14g)</span></div>
            <div class="facts-row facts-row--strong"><span>Calories</span><span>120</span></div>
            <div class="facts-row"><span>Total Fat</span><span>14g</span></div>
            <div class="facts-row"><span>Saturated Fat</span><span>12g</span></div>
            <div class="facts-row"><span>Sodium</span><span>0mg</span></div>
            <div class="facts-row"><span>Protein</span><span>0g</span></div>
          </div>
          <p class="info-text">Ingredients: organic extra virgin coconut oil.<br>
            <strong>Tidewell Pantry</strong><br>
            Product of Mexico<br>
            Net 500 ml<br>
            Store below 24°C</p>
        </div>
      </div>
    </section>

  </main>
</body>
</html>
```